Thank you for exploring whether you are interested in creating a book cover for The Insight Lantern!

The cover should look professional yet appeal to a person who is open to approaching life more deeply.

The logo that I've uploaded is something that you are welcome to use in your book cover design but is not required to be the primary graphic.

The following is a description of The Insight Lantern and its purpose.
RADICAL CLARITY IS POSSIBLE

Are you tired of hitting up against your limitations? Do you wish you could be more effective in everything you do? What would it be like if you could walk confidently into any situation and automatically comprehend it, organize your thoughts, and respond creatively? This kind of radical clarity is not only possible, it’s right in front of you—and The Insight Lantern: Notice Every Signal. Hold Bold Dialogues. Build the Path You Choose. shows you the pathway to get there!

In the book, Dr. Gavin Terlecki draws on over 30 years of experience with executive coaching and leadership development to deliver priceless wisdom about how to see clearly in today’s complex and uncertain world. Using his Insight Lantern, you’ll discover where you’re stuck and why, find your authentic direction, and learn to engage creatively with life so you can start getting what you really want.

A TRANSFORMATIONAL TOOL

The Insight Lantern is a cutting-edge leadership development tool that supports you to activate your maximum potential, both personally and professionally. It’s based on the idea that there are four fundamental building blocks to reality: Intentions, Actions, Facts, and Stories. Understanding the differences between these dimensions of your experience and learning how they work together is the key to forging a clear path toward your destination in life. The Insight Lantern organizes these four main building blocks around the two polarities of a compass:

1. North to South – Intentions to Actions
We all have billions of intentions, but how many do we actually put into action? In this polarity you learn to notice and implement your intentions in order to generate more effective actions and create meaningful outcomes in your life.

2. East vs. West – Facts vs. Stories
We all create stories to make sense of life, but how many of us actually get clear on the facts to see where our stories might be off? In this polarity you learn to discern the objective facts from your subjective interpretations and stories, illuminating a clearer perspective to uncover what’s been blocking you on the path to success.

Using The Insight Lantern you’ll discover how naming and implementing your intentions in life naturally results in more effective behavior and actions, and how distinguishing the real facts from your interpretations of any situation can propel you toward radical clarity and true fulfillment.

BOLD DIALOGUES

The key benefit of using The Insight Lantern is that you’ll have more of what Gavin calls “Bold Dialogues.” Bold Dialogues are those that move you closer to what you’re wanting in life—the kind of human-to-human interactions that actually make a difference. By applying The Insight Lantern, you gain critical insight that opens your eyes to new opportunities for Bold Dialogues, helping you draw on your imagination and move beyond your current stance toward a positive outcome. Every conversation is a possibility waiting to be discovered. The more Bold Dialogues you have, the more profound and meaningful shifts you activate in your life.

PRACTICAL GUIDANCE

The book doesn’t just give you a theoretical understanding of how to gain more clarity in your life. Dr. Terlecki provides you with clear, practical steps to develop the core competencies you need to start getting the results you want. As you explore the book, you’ll find:

• A thorough description of all the directions of The Insight Lantern, each with three main points to focus your energy on.
• Case studies from Gavin’s many clients who have successfully used The Insight Lantern to transform their own lives.
• Hands-on practices Gavin has developed to help you put your new skills to use immediately.
• Step-by-step guidance to apply The Insight Lantern in any situation, including real-life stories from people who have experienced genuine transformation using this tool.

The Insight Lantern will help you to deepen your understanding of the challenges in your life, integrate new competencies to boost your effectiveness, and awaken to exciting opportunities for your own growth, leadership, and success!

ABOUT THE AUTHOR

Dr. Gavin Terlecki has over 30 years of experience with leadership development and executive coaching work. As owner and principal coach of Terlecki Growth Advisors, he has been integrating the fields of management consulting, business psychology, and leadership coaching since 1983. Gavin holds a Ph.D. in psychodynamic and group psychology from the Halvern Graduate Academy, an M.A. in human growth and potential from the Marlowe Ridge University, and a B.A. in accounting and Business Administration from Denby Valley University. He is the creator of The Insight Lantern™, a leadership development tool that supports people to see life clearly, wake up to exciting opportunities for their own growth and leadership, and take empowered action toward true success. Gavin’s combination of business expertise, human compassion, and incisive questions help his clients achieve unprecedented results.

Target Market(s)

Out intended audience is folks who would like to be more effective and to grow and transform. This being more productive and developing could be in their careers or their personal lives.

Industry/Entity Type

It Professional

Requirements
Must have
• Stock images, if used, that I can purchase exclusively or that you can easily create specifically for the book once you are the chosen designer. I completely understand using stock imaging in your submissions pre-selection.
Nice to have
• Ideally the cover will include both the title and subtitle.

```html
<!DOCTYPE html>
<html lang="en">
<head>
<meta charset="utf-8">
<title>The Insight Lantern – Book Cover</title>
<link rel="stylesheet" href="https://fonts.googleapis.com/css2?family=Arimo:wght@400;700&family=Bitter:wght@700&family=Overlock:wght@700;900&display=swap">
<style>
  :root {
    --back-top: #c4917a;
    --back-mid: #a88c77;
    --back-bottom: #858070;
    --spine-top: #ffffff;
    --spine-bottom: #5a4636;
    --ink: #111111;
    --white: #ffffff;
    --band-grey: rgba(120, 118, 112, 0.72);
    --subtitle-grey: #5a5753;
    --author-band: #2e2720;
    --glass-a: #8a8a62;
    --glass-b: #b9b6a2;
    --glass-c: #6f7560;
    --leaf-a: #7fae4a;
    --leaf-b: #cfe0a6;
  }
  * { margin: 0; padding: 0; box-sizing: border-box; }
  html, body { width: 1200px; height: 873px; overflow: hidden; background: #ffffff; }
  .cover { position: relative; width: 1200px; height: 873px; overflow: hidden; }

  /* Back cover */
  .back {
    position: absolute; left: 0; top: 0; width: 545px; height: 873px;
    background: linear-gradient(180deg, var(--back-top) 0%, var(--back-mid) 55%, var(--back-bottom) 100%);
  }
  .back__band { position: absolute; left: 0; top: 614px; width: 545px; height: 107px; background: var(--white); }
  .mark {
    position: absolute; background: var(--white);
    display: flex; align-items: center; justify-content: center; text-align: center;
    font-family: "Arimo", sans-serif; font-weight: 700; font-size: 11px; line-height: 1.15; color: var(--ink);
  }
  .back__mark { left: 51px; top: 40px; width: 69px; height: 69px; }
  .back__heading {
    position: absolute; left: 48px; top: 116px; width: 480px;
    font-family: "Arimo", sans-serif; font-weight: 700; font-size: 27.5px; line-height: 38px; color: var(--ink);
  }
  .back__blurb {
    position: absolute; left: 48px; top: 287px; width: 492px;
    font-family: "Arimo", sans-serif; font-weight: 400; font-size: 24px; line-height: 32.8px; color: var(--ink);
  }

  /* Spine */
  .spine {
    position: absolute; left: 545px; top: 0; width: 108px; height: 873px;
    background: linear-gradient(180deg, var(--spine-top) 0%, #c9c2bc 40%, var(--spine-bottom) 100%);
  }
  .spine__title {
    position: absolute; left: 54px; top: 410px; transform: translate(-50%, -50%) rotate(-90deg);
    white-space: nowrap; font-family: "Overlock", sans-serif; font-weight: 900; font-size: 62px; line-height: 1;
  }
  .spine__title .dark { color: var(--ink); }
  .spine__title .light { color: var(--white); }
  .spine__mark { left: 20px; top: 721px; width: 68px; height: 68px; }

  /* Front cover */
  .front { position: absolute; left: 653px; top: 0; width: 547px; height: 873px; }
  .front__photo {
    position: absolute; inset: 0;
    background:
      radial-gradient(ellipse at 30% 20%, var(--glass-b) 0%, transparent 50%),
      linear-gradient(180deg, var(--glass-c) 0%, var(--glass-a) 35%, var(--glass-b) 100%);
  }
  .front__inset {
    position: absolute; left: 332px; top: 162px; width: 260px; height: 258px; border-radius: 50%;
    border: 5px solid var(--ink);
    background: radial-gradient(circle at 45% 55%, var(--leaf-b) 0%, var(--leaf-a) 60%, #4e7a2c 100%);
  }
  .front__titleband { position: absolute; left: 0; top: 437px; width: 547px; height: 177px; background: var(--band-grey); }
  .front__title { position: absolute; inset: 0; font-family: "Overlock", sans-serif; font-weight: 900; line-height: 1; }
  .front__the { position: absolute; left: 9px; top: 448px; font-size: 46px; color: var(--white); }
  .front__initial { position: absolute; left: 82px; top: 338px; font-size: 220px; color: var(--ink); }
  .front__rest { position: absolute; left: 140px; top: 458px; font-size: 76px; color: var(--ink); }
  .front__lantern { position: absolute; right: 88px; top: 535px; font-size: 62px; color: var(--white); }
  .front__subband { position: absolute; left: 0; top: 614px; width: 547px; height: 107px; background: var(--white); }
  .front__subtitle {
    position: absolute; left: 45px; top: 619px;
    font-family: "Bitter", serif; font-weight: 700; font-size: 23px; line-height: 32.5px; color: var(--subtitle-grey);
  }
  .front__authorband {
    position: absolute; left: 0; top: 806px; width: 547px; height: 36px; background: var(--author-band);
    display: flex; align-items: center; justify-content: center;
    font-family: "Arimo", sans-serif; font-size: 25px; letter-spacing: 2.5px; color: var(--white);
  }
</style>
</head>
<body>
<main class="cover">
  <section class="back">
    <div class="back__band"></div>
    <div class="mark back__mark">Insight<br>Lantern</div>
    <h2 class="back__heading">The Insight Lantern:<br>Notice Every Signal.<br>Hold Bold Dialogues.<br>Build the Path You Choose.</h2>
    <p class="back__blurb">Are you tired of hitting up against your limitations? Do you wish you could be more effective in everything you do? What would it be like if you could walk confidently into any situation and automatically comprehend it, organize your thoughts, and respond creatively? This kind of radical clarity is not only possible, it’s right in front of you—and The Insight Lantern: Notice Every Signal. Hold Bold Dialogues. Build the Path You Choose. shows you the pathway to get there!</p>
  </section>

  <section class="spine">
    <div class="spine__title"><span class="dark">The</span> <span class="light">Insight</span> <span class="dark">Lantern</span></div>
    <div class="mark spine__mark">Insight<br>Lantern</div>
  </section>

  <section class="front">
    <div class="front__photo" role="img" aria-label="Photograph of a textured leaded stained-glass window in green, grey and amber tones"></div>
    <div class="front__inset" role="img" aria-label="Oval inset photograph of dark berries with water droplets among green leaves"></div>
    <div class="front__titleband"></div>
    <h1 class="front__title">
      <span class="front__the">The</span>
      <span class="front__initial">I</span>
      <span class="front__rest">nsight</span>
      <span class="front__lantern">Lantern</span>
    </h1>
    <div class="front__subband"></div>
    <p class="front__subtitle">Notice Every Signal.<br>Hold Bold Dialogues.<br>Build the Path You Choose.</p>
    <div class="front__authorband">Dr. Gavin Terlecki</div>
  </section>
</main>
</body>
</html>
```